Visitenkarten-Design für Yogakurse
Zielgruppe
Ich biete Yogakurse für alle an sowieso speziell Yogakurse für Schwangere, frischgebackene Mamas und Rückbildungskurse.
Meine Zielgruppe sind hauptsächlich schwangere Frauen sowieso Frauen mit Babys.
Aufgabenstellung
Folgende Informationen sollten enthalten sein:
Ruhe im Atem
Yoga & Beckenbodentraining
Henrike Wolmsen
info@ruhe-im-atem-beispiel.de
www.ruhe-im-atem-beispiel.de

```html
<!DOCTYPE html>
<html lang="de">
<head>
<meta charset="utf-8">
<title>Ruhe im Atem – Visitenkarten</title>
<link rel="stylesheet" href="https://fonts.googleapis.com/css2?family=Cinzel:wght@400&family=Poppins:wght@400;500&display=swap">
<style>
  :root {
    --backdrop: #c4c4c4;
    --card-black: #141414;
    --gold: #c9a35a;
    --sage: #d4e3c3;
    --sage-light: #e3eed8;
    --edge-white: #f4f4f2;
  }
  * { box-sizing: border-box; margin: 0; padding: 0; }
  html, body { width: 1200px; height: 800px; overflow: hidden; }
  body {
    background: var(--backdrop);
    position: relative;
    font-family: "Poppins", sans-serif;
  }
  .card {
    position: absolute;
    top: 340px;
    width: 480px;
    height: 273px;
    background: var(--card-black);
    overflow: hidden;
  }
  .card--front { left: 98px; }
  .card--back { left: 614px; }
  .card__wave { position: absolute; inset: 0; width: 100%; height: 100%; }

  .brand {
    position: absolute;
    display: flex;
    flex-direction: column;
    align-items: center;
    gap: 10px;
    transform: translateX(-50%);
  }
  .brand__dot {
    width: 26px; height: 26px;
    border-radius: 50%;
    background: var(--sage);
  }
  .brand__name {
    font-family: "Cinzel", serif;
    font-weight: 400;
    color: var(--gold);
    font-size: 22px;
    letter-spacing: 1px;
    white-space: nowrap;
  }
  .card--front .brand { left: 237px; top: 40px; }
  .card--back .brand { left: 98px; top: 82px; }

  .front__rule {
    position: absolute;
    left: 25px; width: 418px; top: 135px;
    height: 1px; background: var(--sage);
  }
  .front__tagline {
    position: absolute;
    left: 0; width: 480px; top: 144px;
    text-align: center;
    font-family: "Cinzel", serif;
    color: var(--gold);
    font-size: 16px;
    letter-spacing: 4px;
  }

  .back__divider {
    position: absolute;
    left: 190px; top: 39px;
    width: 3px; height: 170px;
    background: var(--sage);
    border-radius: 2px;
  }
  .back__name {
    position: absolute;
    left: 217px; top: 38px;
    font-family: "Cinzel", serif;
    color: var(--gold);
    font-size: 15px;
    letter-spacing: 3px;
  }
  .back__role {
    position: absolute;
    left: 217px; top: 70px;
    color: var(--sage-light);
    font-size: 12.5px;
    font-weight: 500;
  }
  .contact-list {
    position: absolute;
    left: 216px; top: 116px;
    list-style: none;
    display: flex;
    flex-direction: column;
    gap: 15px;
  }
  .contact-list__item {
    display: flex;
    align-items: center;
    gap: 11px;
    color: var(--gold);
    font-size: 13.5px;
    height: 20px;
  }
  .contact-list__icon { width: 18px; height: 18px; flex: none; }
</style>
</head>
<body>

  <section class="card card--front" aria-label="Vorderseite">
    <svg class="card__wave" viewBox="0 0 480 273" aria-hidden="true">
      <path d="M0 222 C150 250 330 248 480 178 L480 273 L0 273 Z" fill="var(--sage)"/>
      <path d="M0 220 C150 248 330 246 480 176" fill="none" stroke="var(--edge-white)" stroke-width="5"/>
    </svg>
    <div class="brand">
      <span class="brand__dot"></span>
      <span class="brand__name">Ruhe im Atem</span>
    </div>
    <div class="front__rule"></div>
    <p class="front__tagline">YOGA &amp; BECKENBODENTRAINING</p>
  </section>

  <section class="card card--back" aria-label="Rückseite">
    <svg class="card__wave" viewBox="0 0 480 273" aria-hidden="true">
      <path d="M0 178 C110 240 300 258 480 230 L480 273 L0 273 Z" fill="var(--sage)"/>
      <path d="M0 176 C110 238 300 256 480 228" fill="none" stroke="var(--edge-white)" stroke-width="5"/>
    </svg>
    <div class="brand">
      <span class="brand__dot"></span>
      <span class="brand__name">Ruhe im Atem</span>
    </div>
    <div class="back__divider"></div>
    <h1 class="back__name">HENRIKE WOLMSEN</h1>
    <p class="back__role">Yoga &amp; Beckenbodentraining</p>
    <ul class="contact-list">
      <li class="contact-list__item">
        <svg class="contact-list__icon" viewBox="0 0 18 18" aria-hidden="true">
          <circle cx="9" cy="9" r="9" fill="var(--sage-light)"/>
          <path d="M6 4.5 L7.6 4.5 L8.2 7 L7.1 7.8 C7.7 9.1 8.9 10.3 10.2 10.9 L11 9.8 L13.5 10.4 L13.5 12 C13.5 12.8 12.8 13.5 12 13.4 C8.2 13 5 9.8 4.6 6 C4.5 5.2 5.2 4.5 6 4.5 Z" fill="var(--card-black)"/>
        </svg>
        0170 - 4839261
      </li>
      <li class="contact-list__item">
        <svg class="contact-list__icon" viewBox="0 0 18 18" aria-hidden="true">
          <circle cx="9" cy="9" r="9" fill="var(--sage-light)"/>
          <rect x="4.5" y="5.8" width="9" height="6.4" rx="0.8" fill="none" stroke="var(--card-black)" stroke-width="1.2"/>
          <path d="M4.8 6.2 L9 9.4 L13.2 6.2" fill="none" stroke="var(--card-black)" stroke-width="1.2"/>
        </svg>
        info@ruhe-im-atem-beispiel.de
      </li>
      <li class="contact-list__item">
        <svg class="contact-list__icon" viewBox="0 0 18 18" aria-hidden="true">
          <circle cx="9" cy="9" r="9" fill="var(--sage-light)"/>
          <g fill="none" stroke="var(--card-black)" stroke-width="1.1">
            <circle cx="9" cy="9" r="4.6"/>
            <ellipse cx="9" cy="9" rx="2" ry="4.6"/>
            <path d="M4.4 9 H13.6"/>
          </g>
        </svg>
        www.ruhe-im-atem-beispiel.de
      </li>
    </ul>
  </section>

</body>
</html>
```